Need a Modern WIX Website design

Need help designing a modern WIX website. I already started building on editor.wix.com but I am not a designer and would like a more modern, update aesthetic look. This is not an e-commerce site. Just a website portraying our company, posting what products we offer, contact, about us, services. Logo is already on the editor.wix version with some content. Need a designer with vision, and ingenuity to set it apart change it a little and make it stand out. Please look at the current site for redesign and/or ideas https://corvadetradewks.sitebuildr.net/website
also need the design to be connected to our google domain www.ctw.supply

Please feel free to ask as many questions as possible

Target Market(s)

Tire repair shops, Tire stores, mechanic shops, tire replacement franchises, wheel and rim stores

Industry/Entity Type

we are wholesalers, B2B ..sell tire repair materials, tire hand tools, machinery, chemicals, wheel lug nuts, wheel accessories

Coding

Coded - Design and coding required

Number of Pages Required

5+ page

Font styles to use
Other font styles liked:
• Let designer choose

Colors

Designer to choose colors to be used in the design.

Requirements
Must have
• modern design layout, videos, high quality pictures, different ideas for pages (Home, shop, about, products, services, contact, faq, meet the team) translatable english to spanish
Nice to have
• would like to have an up to date modern look, interactive, easy to navigate,
Should not have
• not be hard to navigate for our customers

```html
<!DOCTYPE html>
<html lang="en">
<head>
<meta charset="utf-8">
<title>Corvade Trade Works — Tire Repair Supplies</title>
<link rel="stylesheet" href="https://fonts.googleapis.com/css2?family=Poppins:wght@400;500;600;700&family=Rajdhani:wght@600;700&display=swap">
<style>
:root{
  --red:#e0201f;
  --red-dark:#b3121a;
  --black:#0e0e0f;
  --charcoal:#1c1c1e;
  --graphite:#2b2b2e;
  --light:#efefef;
  --white:#ffffff;
  --text:#333338;
  --muted:#8a8a8f;
}
*{box-sizing:border-box;margin:0;padding:0}
html,body{width:1200px;height:4520px;overflow:hidden}
body{position:relative;background:var(--white);font-family:"Poppins",sans-serif;color:var(--text)}
.abs{position:absolute}
.heading{font-family:"Rajdhani",sans-serif;font-weight:700;font-size:46px;text-align:center;letter-spacing:.5px}
.heading .accent{color:var(--red)}
.btn{display:inline-block;background:var(--red);color:var(--white);font-size:13px;font-weight:600;padding:12px 26px;border-radius:3px}
.brandname{font-family:"Poppins",sans-serif;font-weight:700;color:var(--white);font-size:30px;letter-spacing:1px;display:flex;align-items:center;gap:10px}
.brandname .mark{width:22px;height:22px;background:var(--red)}

/* hero */
.hero{left:0;top:0;width:1200px;height:660px;overflow:hidden}
.hero-photo{position:absolute;inset:0;background:radial-gradient(circle at 80% 35%,#c0391f 0%,#5a1d14 22%,#1c1c1e 48%,#0b0b0c 80%)}
.hero-topline{position:absolute;left:0;top:0;width:1200px;height:8px;background:var(--red)}
.topbar{position:absolute;left:160px;top:16px;width:880px;height:30px}
.topbar .contact{position:absolute;right:0;top:6px;display:flex;gap:28px;font-size:12px;color:var(--white)}
.topbar .contact span{display:flex;align-items:center;gap:8px}
.nav{position:absolute;right:160px;top:70px;display:flex;gap:44px;font-size:13px;font-weight:500;color:var(--white);text-transform:uppercase}
.logo-slot{position:absolute;left:160px;top:30px}
.hero-title{position:absolute;left:160px;top:232px;font-family:"Poppins",sans-serif;font-style:italic;font-weight:700;font-size:52px;line-height:64px;color:var(--white)}
.hero .btn{position:absolute;left:160px;top:452px}
.hero-edge{position:absolute;left:0;top:520px}

/* about */
.about-photo{left:160px;top:920px;width:360px;height:320px;background:linear-gradient(135deg,#b9b6b2,#5f5a56 55%,#2f2c2b);border:8px solid var(--white);box-shadow:0 0 0 2px #e6e6e6}
.about-frame{left:150px;top:910px;width:60px;height:60px;border-left:6px solid var(--red);border-top:6px solid var(--red)}
.about-text{left:640px;top:920px;width:440px}
.about-text .brandname{color:var(--black);margin-bottom:28px}
.about-text p{font-size:13px;line-height:22px;color:var(--text);margin-bottom:18px}

/* brands */
.brands{left:0;top:1300px;width:1200px;height:520px}
.brands-title{left:0;top:1420px;width:1200px;color:var(--white)}
.brand-row{left:160px;top:1510px;width:880px;display:flex;justify-content:space-between}
.brand{width:160px;text-align:center;color:var(--white);font-size:12px}
.brand .tile{width:160px;height:120px;background:var(--graphite);display:flex;align-items:center;justify-content:center;margin-bottom:12px}
.brand .tile i{width:70px;height:70px;border:2px solid #bdbdbd;border-radius:50%}
.arrow{width:40px;height:40px;display:flex;align-items:center;justify-content:center}

/* products */
.products{left:0;top:1780px;width:1200px;height:560px;background:var(--light)}
.products-title{left:0;top:1830px;width:1200px;color:var(--black)}
.product-row{left:180px;top:1920px;width:840px;display:flex;justify-content:space-between}
.product{width:190px;height:280px;text-align:center;font-size:12px;line-height:18px;color:var(--text);padding:14px}
.product.active{background:var(--white);box-shadow:0 6px 18px rgba(0,0,0,.15)}
.product.active .pname{color:var(--red)}
.product .shot{height:170px;margin:0 auto 14px;border-radius:6px}
.products .btn{position:absolute;left:536px;top:438px}
.circle-arrow{width:38px;height:38px;border-radius:50%;background:var(--white);box-shadow:0 2px 6px rgba(0,0,0,.2);display:flex;align-items:center;justify-content:center}

/* services */
.services{left:0;top:2340px;width:1200px;height:780px}
.services-title{left:0;top:2430px;width:1200px;color:var(--white)}
.service-row{left:160px;top:2540px;width:880px;display:flex;justify-content:space-between}
.service{width:280px;text-align:center;position:relative}
.service .shot{height:280px;margin-top:30px}
.service .icon{position:absolute;left:110px;top:0;width:60px;height:60px;background:var(--red-dark);border:3px solid var(--white);display:flex;align-items:center;justify-content:center}
.service.featured .icon{background:var(--white);border-color:var(--red)}
.service.featured .shot{outline:3px solid var(--white)}
.service h3{font-size:18px;font-weight:600;color:var(--white);margin-top:22px}
.service.featured h3{color:var(--red)}
.services-btn{left:540px;top:2950px}

/* faq */
.faq-title{left:0;top:3172px;width:1200px;color:var(--black)}
.faq-list{left:240px;top:3268px;width:720px}
.faq-item{border:1px solid #d8d8d8;border-radius:6px;margin-bottom:16px;padding:16px 20px;position:relative;font-size:12px;font-weight:600;color:var(--black)}
.faq-item .toggle{position:absolute;right:16px;top:13px;width:22px;height:22px;border-radius:50%;background:var(--black);color:var(--white);font-size:14px;line-height:21px;text-align:center}
.faq-item.open .q{color:var(--red)}
.faq-item p{font-weight:400;font-size:12px;line-height:20px;color:var(--text);margin-top:12px;padding-right:30px}

/* map */
.map{left:160px;top:3700px;width:880px;height:420px;background:linear-gradient(135deg,#e4e4e4,#cfcfcf 55%,#dedede)}
.map-card{left:540px;top:3800px;width:240px;background:var(--white);box-shadow:0 3px 10px rgba(0,0,0,.2);padding:14px 16px 14px 40px;font-size:11px;line-height:16px}
.map-card strong{display:block;color:var(--black)}
.map-card span{color:var(--red)}

/* footer */
.footer{left:0;top:4140px;width:1200px;height:340px;background:var(--black);color:var(--white)}
.footer .col{position:absolute;top:40px;font-size:12px;line-height:22px}
.footer h4{color:var(--red);font-size:16px;font-weight:600;margin-bottom:10px}
.footer .hours{font-size:12px;line-height:20px}
.footer .hours b{display:block;color:var(--white);font-weight:600}
.socials{display:flex;gap:14px;margin-top:6px}
.socials i{width:14px;height:14px;border-radius:50%;background:var(--white)}
.detail{display:flex;gap:12px;margin-bottom:14px}
.detail .ic{width:24px;height:24px;border-radius:50%;background:var(--red);display:flex;align-items:center;justify-content:center;flex:none}
.copyright{left:0;top:4480px;width:1200px;height:40px;background:var(--red);color:var(--white);font-size:11px;padding:0 160px;display:flex;align-items:center;justify-content:space-between}
</style>
</head>
<body>

<!-- Hero -->
<section class="abs hero">
  <div class="hero-photo" role="img" aria-label="Garage interior with a mounted tire and wheel lit by warm red light"></div>
  <div class="hero-topline"></div>
  <div class="logo-slot"><div class="brandname"><i class="mark"></i>CORVADE</div></div>
  <div class="topbar">
    <div class="contact">
      <span><svg width="12" height="12" viewBox="0 0 24 24"><rect x="2" y="5" width="20" height="14" rx="2" fill="none" stroke="#e0201f" stroke-width="2"/><path d="M2 6l10 7 10-7" fill="none" stroke="#e0201f" stroke-width="2"/></svg>customerservice@ctw.supply</span>
      <span><svg width="12" height="12" viewBox="0 0 24 24"><path d="M6 2l4 4-2 3c1 3 4 6 7 7l3-2 4 4-3 4C10 22 2 14 2 5z" fill="#e0201f"/></svg>833-555-0142</span>
    </div>
  </div>
  <nav class="nav"><span>Home</span><span>Shop</span><span>About</span><span>Services</span><span>Contact</span><span>FAQ</span><span>Team</span></nav>
  <h1 class="hero-title">Your One Stop<br>Tire Repair Supplier<br>In New York</h1>
  <span class="btn">Contact Us</span>
  <svg class="hero-edge" width="1200" height="140" viewBox="0 0 1200 140">
    <polygon points="0,90 1200,30 1200,140 0,140" fill="#ffffff"/>
    <polygon points="0,82 1200,22 1200,34 0,94" fill="#e0201f"/>
  </svg>
</section>

<!-- About -->
<div class="abs about-frame"></div>
<div class="abs about-photo" role="img" aria-label="Technician handling a tire in a workshop"></div>
<section class="abs about-text">
  <div class="brandname"><i class="mark"></i>CORVADE TRADE WORKS</div>
  <p>At Corvade Trade Works we make sure to offer our clients the best.</p>
  <p>Selection of tire repair products, tools and machinery as well as provide them with superb customer service. Our staff works with our customers to find exactly the right part they need for the right price. We're here to help inform you about our products so that you only buy what is absolutely necessary for your establishment. Contact us today to learn more about what we do.</p>
  <span class="btn">Read More</span>
</section>

<!-- Brands -->
<svg class="abs brands" viewBox="0 0 1200 520" width="1200" height="520">
  <polygon points="0,40 1200,0 1200,480 0,520" fill="#141415"/>
</svg>
<h2 class="abs heading brands-title">Brands We <span class="accent">Work With</span></h2>
<div class="abs arrow" style="left:90px;top:1550px"><svg width="14" height="24" viewBox="0 0 14 24"><path d="M12 2L2 12l10 10" fill="none" stroke="#fff" stroke-width="2.5"/></svg></div>
<div class="abs arrow" style="left:1070px;top:1550px"><svg width="14" height="24" viewBox="0 0 14 24"><path d="M2 2l10 10L2 22" fill="none" stroke="#fff" stroke-width="2.5"/></svg></div>
<div class="abs brand-row">
  <div class="brand"><div class="tile"><i></i></div>Brightwell Supply</div>
  <div class="brand"><div class="tile"><i></i></div>Northgate Group</div>
  <div class="brand"><div class="tile"><i></i></div>Orvale Tools</div>
  <div class="brand"><div class="tile"><i></i></div>Kestrel Garage Co</div>
  <div class="brand"><div class="tile"><i></i></div>Sandbrook</div>
</div>

<!-- Products -->
<section class="abs products">
  <span class="btn">View All Products</span>
</section>
<h2 class="abs heading products-title">Our <span class="accent">Products</span></h2>
<div class="abs circle-arrow" style="left:110px;top:2020px"><svg width="10" height="14" viewBox="0 0 10 14"><path d="M8 1L2 7l6 6" fill="none" stroke="#333" stroke-width="2"/></svg></div>
<div class="abs circle-arrow" style="left:1052px;top:2020px"><svg width="10" height="14" viewBox="0 0 10 14"><path d="M2 1l6 6-6 6" fill="none" stroke="#333" stroke-width="2"/></svg></div>
<div class="abs product-row">
  <div class="product"><div class="shot" role="img" aria-label="Chrome spline lug nut" style="width:90px;background:linear-gradient(#d8d8d8,#8b8b8b)"></div><div class="pname">Spline Lug Nut<br>Car (6 Sided) – M14 X1.5</div></div>
  <div class="product"><div class="shot" role="img" aria-label="Tin of cold vulcanizing fluid" style="width:120px;background:linear-gradient(#ece6c8,#8a8468)"></div><div class="pname">Quick-Cure Cold Vulcanizing<br>Fluid (Flammable)</div></div>
  <div class="product active"><div class="shot" role="img" aria-label="Black impact flip socket" style="width:80px;background:linear-gradient(#3a3a3a,#111)"></div><div class="pname">Heavy Duty Tire Wall<br>Impact Flip Socket</div></div>
  <div class="product"><div class="shot" role="img" aria-label="Brown surface conditioning disc" style="width:150px;height:150px;border-radius:50%;background:radial-gradient(#2a2520 18%,#6b5a48 22%,#3d3228)"></div><div class="pname">50 Pk 2" Coarse Brown<br>Surface Conditioning</div></div>
</div>

<!-- Services -->
<svg class="abs services" viewBox="0 0 1200 780" width="1200" height="780">
  <polygon points="0,0 1200,40 1200,740 0,780" fill="#151516"/>
</svg>
<h2 class="abs heading services-title">Our <span class="accent">Services</span></h2>
<div class="abs service-row">
  <div class="service">
    <div class="shot" role="img" aria-label="Staff member assisting a customer at a tire counter" style="background:linear-gradient(135deg,#9aa3ad,#4a4f56)"></div>
    <div class="icon"><svg width="28" height="28" viewBox="0 0 24 24"><circle cx="12" cy="9" r="4" fill="none" stroke="#fff" stroke-width="2"/><path d="M4 21c1-5 15-5 16 0" fill="none" stroke="#fff" stroke-width="2"/></svg></div>
    <h3>Stellar Customer Service</h3>
  </div>
  <div class="service featured">
    <div class="shot" role="img" aria-label="Close view of stacked tire treads" style="background:linear-gradient(135deg,#3a3a3c,#0d0d0e)"></div>
    <div class="icon"><svg width="28" height="28" viewBox="0 0 24 24"><circle cx="12" cy="10" r="6" fill="none" stroke="#e0201f" stroke-width="2"/><path d="M8 15l-2 7 6-3 6 3-2-7" fill="none" stroke="#e0201f" stroke-width="2"/></svg></div>
    <h3>High Quality Products</h3>
  </div>
  <div class="service">
    <div class="shot" role="img" aria-label="Two people shaking hands in a garage" style="background:linear-gradient(135deg,#5b7fa8,#2b3c55)"></div>
    <div class="icon"><svg width="28" height="28" viewBox="0 0 24 24"><path d="M2 12l5-5 5 4 5-4 5 5-8 7z" fill="none" stroke="#fff" stroke-width="2"/></svg></div>
    <h3>Commitment</h3>
  </div>
</div>
<span class="abs btn services-btn">Contact Us</span>

<!-- FAQ -->
<h2 class="abs heading faq-title">Frequently <span class="accent">Asked Questions</span></h2>
<div class="abs faq-list">
  <div class="faq-item"><span class="q">What Is Your Return Policy ?</span><span class="toggle">+</span></div>
  <div class="faq-item open"><span class="q">Do You Provide Repairs ?</span><span class="toggle">−</span>
    <p>Lorem ipsum dolor sit amet, consectetuer adipiscing elit, sed diam nonummy nibh euismod tincidunt ut laoreet dolore magna aliquam erat volutpat. Ut wisi enim ad minim veniam, quis nostrud exerci tation ullamcorper suscipit lobortis nisl ut aliquip.</p></div>
  <div class="faq-item"><span class="q">When Is Your Next Big Sale ?</span><span class="toggle">+</span></div>
  <div class="faq-item"><span class="q">Is There Free Delivery Possible ?</span><span class="toggle">+</span></div>
</div>

<!-- Map -->
<div class="abs map" role="img" aria-label="Street map around the warehouse location"></div>
<svg class="abs" style="left:520px;top:3812px" width="20" height="26" viewBox="0 0 24 30"><path d="M12 0C5 0 1 5 1 11c0 8 11 19 11 19s11-11 11-19C23 5 19 0 12 0z" fill="#e0201f"/><circle cx="12" cy="11" r="4" fill="#fff"/></svg>
<div class="abs map-card"><strong>Corvade Trade Works</strong><span>410 Harbor Point Street<br>San Francisco<br>CA 94107</span></div>

<!-- Footer -->
<footer class="abs footer">
  <div class="col" style="left:160px">
    <div class="brandname" style="font-size:26px;margin-bottom:18px"><i class="mark"></i>CORVADE</div>
    <h4>Working Hours</h4>
    <div class="hours"><b>Mon – Fri</b>9 a.m. – 5 p.m.<br><b style="margin-top:8px">Sat – Sun</b>Close</div>
  </div>
  <div class="col" style="left:540px">
    <h4>Quick Links</h4>
    Home<br>Shop<br>About<br>Services<br>Contact<br>FAQs<br>Team
  </div>
  <div class="col" style="left:800px">
    <h4>Contact Details</h4>
    <div class="detail"><span class="ic"><svg width="12" height="14" viewBox="0 0 24 30"><path d="M12 0C5 0 1 5 1 11c0 8 11 19 11 19s11-11 11-19C23 5 19 0 12 0z" fill="#fff"/></svg></span><span>410 Harbor Point Street<br>San Francisco, CA 94107</span></div>
    <div class="detail"><span class="ic"><svg width="12" height="12" viewBox="0 0 24 24"><path d="M6 2l4 4-2 3c1 3 4 6 7 7l3-2 4 4-3 4C10 22 2 14 2 5z" fill="#fff"/></svg></span><span><b style="color:#e0201f">Phone</b><br>833-555-0142</span></div>
    <div class="detail"><span class="ic"><svg width="12" height="12" viewBox="0 0 24 24"><rect x="2" y="5" width="20" height="14" rx="2" fill="#fff"/></svg></span><span><b style="color:#e0201f">Email</b><br>customerservice@ctw.supply</span></div>
  </div>
</footer>
<div class="abs copyright"><span>© 2022 Corvade Trade Works. All Rights Reserved.</span><span class="socials"><i></i><i></i><i></i><i></i></span></div>

</body>
</html>
```